Business Card Design Project

A double sided business card for presentation to business leaders in corporate.

Target Market(s)

Corporate, business professionals, HR

Industry/Entity Type

Business

Requirements
Must have
• FRONT

Logo

www.brightlanecoaching.com.au

BACK

Mara Pollen-Drew
Director

+ 61 (0) 418 536 204
mara@brightlanecoaching.com.au
www.brightlanecoaching.com.au

Impact through energy and employee engagement

("ripples" of logo, bottom corner)

Must be:
- double sided
size: 86 x 54mm
supplied as one pdf with crop marks shown (+- 1mm, with 2-3 mm bleed)

```html
<!DOCTYPE html>
<html lang="en">
<head>
<meta charset="utf-8">
<title>Bright Lane Coaching – Business Card</title>
<link href="https://fonts.googleapis.com/css2?family=Arimo:wght@400;700&display=swap" rel="stylesheet">
<style>
  :root {
    --backdrop: #d6d6d8;
    --plum: #6b1f5c;
    --plum-light: #8a3a7a;
    --plum-deep: #561549;
    --paper: #fbfbfb;
    --ink: #3a3a3c;
    --ink-soft: #5a5a5e;
    --accent-red: #b3262f;
    --ripple: #e4e2e6;
    --divider: #8c8c90;
  }
  * { box-sizing: border-box; margin: 0; padding: 0; }
  html, body {
    width: 1200px; height: 900px; overflow: hidden;
    background: var(--backdrop);
    font-family: "Arimo", Arial, sans-serif;
  }
  .stage {
    position: relative; width: 1200px; height: 900px;
    display: flex; align-items: center; justify-content: center; gap: 60px;
  }
  .card {
    position: relative; width: 480px; height: 301px; overflow: hidden;
    box-shadow: 0 10px 24px rgba(0,0,0,0.18);
  }

  /* Front */
  .card-front {
    background: radial-gradient(ellipse at 50% 40%, var(--plum-light) 0%, var(--plum) 45%, var(--plum-deep) 100%);
    color: #fff;
  }
  .front-brand {
    position: absolute; left: 0; right: 0; top: 112px;
    display: flex; align-items: center; justify-content: center; gap: 12px;
  }
  .brand-dot {
    width: 26px; height: 26px; border-radius: 50%;
    border: 2px solid currentColor;
  }
  .brand-name {
    font-size: 30px; font-weight: 400; letter-spacing: -0.5px; line-height: 1;
  }
  .front-url {
    position: absolute; left: 0; right: 0; bottom: 42px;
    text-align: center; font-size: 11px; letter-spacing: 0.5px; opacity: 0.9;
  }

  /* Back */
  .card-back { background: var(--paper); color: var(--ink); }
  .ripple-field {
    position: absolute; right: -60px; top: -90px; width: 380px; height: 380px;
    border-radius: 50%;
    background: radial-gradient(circle at 70% 30%, var(--ripple) 0%, rgba(228,226,230,0.5) 50%, rgba(251,251,251,0) 72%);
  }
  .back-brand {
    position: absolute; left: 28px; top: 170px;
    display: flex; align-items: center; gap: 8px; color: var(--ink);
  }
  .back-brand .brand-dot { width: 20px; height: 20px; border-color: var(--plum); background: var(--plum); }
  .back-brand .brand-name { font-size: 21px; }
  .back-divider {
    position: absolute; left: 250px; top: 118px; width: 1px; height: 72px;
    background: var(--divider);
  }
  .contact {
    position: absolute; left: 264px; top: 112px;
  }
  .contact-name { font-size: 15px; font-weight: 700; color: var(--ink); }
  .contact-role { font-size: 11px; color: var(--accent-red); margin-top: 3px; margin-bottom: 10px; }
  .contact-list { list-style: none; }
  .contact-list li {
    display: flex; align-items: center; gap: 7px;
    font-size: 10.5px; color: var(--ink-soft); line-height: 16px;
  }
  .contact-list svg { width: 10px; height: 10px; flex: none; }
</style>
</head>
<body>
<main class="stage">
  <section class="card card-front" aria-label="Business card front">
    <div class="front-brand">
      <span class="brand-dot"></span>
      <span class="brand-name">bright lane coaching</span>
    </div>
    <p class="front-url">www.brightlanecoaching.com.au</p>
  </section>

  <section class="card card-back" aria-label="Business card back">
    <div class="ripple-field" role="img" aria-label="Faint ripple decoration in the top corner"></div>
    <div class="back-brand">
      <span class="brand-dot"></span>
      <span class="brand-name">bright lane coaching</span>
    </div>
    <div class="back-divider"></div>
    <div class="contact">
      <p class="contact-name">Mara Pollen-Drew</p>
      <p class="contact-role">Director</p>
      <ul class="contact-list">
        <li>
          <svg viewBox="0 0 10 10" aria-hidden="true"><path d="M2 0.8 L3.6 2.8 L2.8 3.8 Q4 6 6.2 7.2 L7.2 6.4 L9.2 8 L8 9.4 Q3.5 8.8 0.6 2 Z" fill="var(--ink)"/></svg>
          + 61 (0) 418 536 204
        </li>
        <li>
          <svg viewBox="0 0 10 10" aria-hidden="true"><rect x="0.5" y="2" width="9" height="6.5" fill="var(--ink)"/><path d="M0.8 2.3 L5 5.6 L9.2 2.3" stroke="#fff" stroke-width="0.9" fill="none"/></svg>
          mara@brightlanecoaching.com.au
        </li>
        <li>
          <svg viewBox="0 0 10 10" aria-hidden="true"><circle cx="5" cy="5" r="4.3" fill="none" stroke="var(--ink)" stroke-width="1"/><ellipse cx="5" cy="5" rx="1.8" ry="4.3" fill="none" stroke="var(--ink)" stroke-width="0.8"/><line x1="0.7" y1="5" x2="9.3" y2="5" stroke="var(--ink)" stroke-width="0.8"/></svg>
          www.brightlanecoaching.com.au
        </li>
      </ul>
    </div>
  </section>
</main>
</body>
</html>
```